Business Card Design

We are a manufacturing and distribution company with most of our customer base being supermarkets. We have established brand guidelines that are attached.

```html
<!DOCTYPE html>
<html lang="en">
<head>
<meta charset="utf-8">
<title>Veranto Business Card</title>
<link href="https://fonts.googleapis.com/css2?family=Montserrat:wght@400;500;700;800&display=swap" rel="stylesheet">
<style>
  :root {
    --backdrop: #262626;
    --brand-red: #e31b23;
    --brand-red-deep: #c9161d;
    --brand-blue: #1667b0;
    --ink: #111111;
    --muted: #6b6b6b;
    --paper: #ffffff;
  }
  * { box-sizing: border-box; margin: 0; padding: 0; }
  html, body {
    width: 1200px;
    height: 1108px;
    overflow: hidden;
    background: var(--backdrop);
    font-family: "Montserrat", sans-serif;
  }
  .stage {
    position: relative;
    width: 1200px;
    height: 1108px;
  }
  .card {
    position: absolute;
    top: 250px;
    width: 370px;
    height: 600px;
    border-radius: 26px;
    overflow: hidden;
    box-shadow: 0 18px 40px rgba(0,0,0,0.45);
  }
  /* Front */
  .card--front {
    left: 175px;
    background: var(--brand-red);
  }
  .front-pattern {
    position: absolute;
    inset: 0;
    background: linear-gradient(150deg, var(--brand-red-deep) 0%, var(--brand-red) 55%, #d81920 100%);
  }
  .front-wordmark {
    position: absolute;
    left: 0;
    right: 0;
    bottom: 110px;
    text-align: center;
    color: var(--paper);
    font-weight: 700;
    font-size: 34px;
    letter-spacing: 2px;
  }
  /* Back */
  .card--back {
    left: 655px;
    background: var(--paper);
  }
  .contact {
    position: absolute;
    top: 80px;
    right: 34px;
    text-align: right;
  }
  .contact-name {
    color: var(--brand-red);
    font-weight: 800;
    font-size: 30px;
    letter-spacing: 1px;
    line-height: 1.1;
  }
  .contact-role {
    color: var(--ink);
    font-weight: 500;
    font-size: 17px;
    margin-top: 2px;
  }
  .contact-list {
    list-style: none;
    margin-top: 14px;
  }
  .contact-item {
    display: flex;
    justify-content: flex-end;
    align-items: center;
    gap: 9px;
    color: var(--muted);
    font-size: 15px;
    font-weight: 400;
    height: 26px;
  }
  .contact-icon {
    width: 20px;
    height: 20px;
    border-radius: 3px;
    background: var(--brand-blue);
    display: flex;
    align-items: center;
    justify-content: center;
    flex: none;
  }
  .contact-address {
    color: var(--muted);
    font-size: 15px;
    line-height: 1.5;
    margin-top: 6px;
    margin-right: 29px;
  }
  .brand-lockup {
    position: absolute;
    left: 0;
    right: 0;
    bottom: 100px;
    display: flex;
    flex-direction: column;
    align-items: center;
    gap: 18px;
  }
  .brand-square {
    width: 46px;
    height: 46px;
    background: var(--brand-red);
  }
  .brand-name {
    color: var(--ink);
    font-weight: 800;
    font-size: 48px;
    letter-spacing: 2px;
  }
</style>
</head>
<body>
<main class="stage">
  <section class="card card--front">
    <div class="front-pattern" role="img" aria-label="Repeating brand symbol pattern in tonal red"></div>
    <div class="front-wordmark">VERANTO</div>
  </section>

  <section class="card card--back">
    <div class="contact">
      <h1 class="contact-name">DANA REYES</h1>
      <p class="contact-role">Manager</p>
      <ul class="contact-list">
        <li class="contact-item">(555) 014-2288
          <span class="contact-icon">
            <svg width="12" height="12" viewBox="0 0 24 24"><path fill="#fff" d="M6.6 10.8a15.1 15.1 0 0 0 6.6 6.6l2.2-2.2a1 1 0 0 1 1-.25 11.4 11.4 0 0 0 3.6.57 1 1 0 0 1 1 1V20a1 1 0 0 1-1 1A17 17 0 0 1 3 4a1 1 0 0 1 1-1h3.5a1 1 0 0 1 1 1c0 1.25.2 2.45.57 3.57a1 1 0 0 1-.25 1z"/></svg>
          </span>
        </li>
        <li class="contact-item">info@verantomail.com
          <span class="contact-icon">
            <svg width="13" height="10" viewBox="0 0 26 20"><rect x="1.5" y="1.5" width="23" height="17" fill="none" stroke="#fff" stroke-width="2.5"/><path d="M2 2l11 9 11-9" fill="none" stroke="#fff" stroke-width="2.5"/></svg>
          </span>
        </li>
        <li class="contact-item">www.veranto.com
          <span class="contact-icon">
            <svg width="11" height="13" viewBox="0 0 22 26"><path fill="#fff" d="M3 1l16 14h-7l4 9-3 1.5-4-9-6 5z"/></svg>
          </span>
        </li>
      </ul>
      <p class="contact-address">48 Harbor Ave. Suite 210<br>Millbrook, TX 0000</p>
    </div>

    <div class="brand-lockup">
      <span class="brand-square"></span>
      <span class="brand-name">VERANTO</span>
    </div>
  </section>
</main>
</body>
</html>
```